Letterhead for financial advisor-insurance agent firm

Our company, Marlowe Thistle Insurance & Investments, is an insurance (health, life, home, auto, etc) and investment brokerage offering a suite of options to meet client needs. We need letterhead that is professional and embodies strength, security and sophistication.

Industry/Entity Type

Investment

```html
<!DOCTYPE html>
<html lang="en">
<head>
<meta charset="utf-8">
<title>Marlowe Thistle Insurance &amp; Investments — Letterhead</title>
<link rel="stylesheet" href="https://fonts.googleapis.com/css2?family=Cinzel:wght@500&display=swap">
<style>
  :root {
    --paper: #ffffff;
    --page-edge: #7a7a7a;
    --navy: #2b3350;
    --slate: #6b7a80;
    --ink: #2b3350;
  }
  * { margin: 0; padding: 0; box-sizing: border-box; }
  html, body {
    width: 854px;
    height: 1200px;
    overflow: hidden;
    background: var(--paper);
  }
  .letterhead {
    position: relative;
    width: 854px;
    height: 1200px;
    background: var(--paper);
  }
  .page-frame {
    position: absolute;
    left: 10px;
    top: 10px;
    right: 10px;
    bottom: 6px;
    border: 1.5px solid var(--page-edge);
  }
  .brand {
    position: absolute;
    top: 61px;
    left: 0;
    width: 100%;
    display: flex;
    flex-direction: column;
    align-items: center;
    font-family: "Cinzel", "Times New Roman", serif;
    font-weight: 500;
    color: var(--ink);
  }
  .brand-mark {
    width: 48px;
    height: 48px;
    border: 2.5px solid var(--ink);
    margin-bottom: 7px;
  }
  .brand-name {
    font-size: 20px;
    letter-spacing: 0.5px;
    line-height: 1;
  }
  .brand-tagline {
    font-size: 8px;
    letter-spacing: 0.4px;
    line-height: 1;
    margin-top: 4px;
  }
  .footer-band {
    position: absolute;
    left: 11px;
    right: 11px;
  }
  .footer-band--slate {
    top: 1112px;
    height: 14px;
    background: var(--slate);
  }
  .footer-band--navy {
    top: 1130px;
    bottom: 7px;
    background: var(--navy);
  }
</style>
</head>
<body>
  <main class="letterhead">
    <div class="page-frame"></div>

    <header class="brand">
      <div class="brand-mark"></div>
      <div class="brand-name">Marlowe Thistle</div>
      <div class="brand-tagline">Insurance &amp; Investments</div>
    </header>

    <div class="footer-band footer-band--slate"></div>
    <div class="footer-band footer-band--navy"></div>
  </main>
</body>
</html>
```